Marlow Crest Group (Real Estate and Investment)

A high end, clean design.
We are a real estate company with sales, asset management and investment divisions. We want to use a black and white scheme which is really high end feel. The back of the card can just be the logo (black background with the white writing) as we will probably emboss this when we print)

Target Market(s)

High level investors, high end houses for sale

Industry/Entity Type

Business

Contact Information for Business Card

Name, position, phone number and email address
Glen Varley, Managing Director, 0437259064 and glen@marlowcrest-example.com.au

Requirements
Must have
• Back of the card to be the black background with the white writing (as per the attached images). Would like the capacity to emboss the writing and logo

```html
<!DOCTYPE html>
<html lang="en">
<head>
<meta charset="utf-8">
<title>Marlow Crest Group — Business Card</title>
<link href="https://fonts.googleapis.com/css2?family=Open+Sans:wght@400;600;700&display=swap" rel="stylesheet">
<style>
  :root {
    --ink: #363435;
    --ink-deep: #1e1d1e;
    --paper: #ffffff;
    --canvas: #ffffff;
    --rule: #555355;
    --reverse-text: #f2f2f2;
  }
  * { margin: 0; padding: 0; box-sizing: border-box; }
  html, body {
    width: 1074px; height: 1200px; overflow: hidden;
    background: var(--canvas);
    font-family: "Open Sans", Arial, sans-serif;
  }
  .canvas { position: relative; width: 1074px; height: 1200px; }

  .card {
    position: absolute; left: 114px; width: 849px; height: 449px;
    background: var(--paper);
    border: 1px solid var(--rule);
    overflow: hidden;
  }
  .card--back { top: 137px; background: var(--ink); border-color: var(--ink); }
  .card--front { top: 616px; }

  .brand-mark {
    position: absolute; border: 2px solid var(--ink); border-radius: 50%;
  }
  .brand-name {
    position: absolute; white-space: nowrap;
    font-weight: 600; color: var(--ink); letter-spacing: 0.5px;
    text-align: center;
  }

  .card--back .brand-mark { left: 349px; top: 81px; width: 150px; height: 150px; border-color: var(--reverse-text); }
  .card--back .brand-name { left: 0; width: 849px; top: 277px; font-size: 33px; color: var(--reverse-text); }

  .card-band {
    position: absolute; left: 0; bottom: 0; width: 100%; height: 67px;
    background: var(--ink-deep); color: var(--reverse-text);
    font-size: 19px; display: flex; align-items: center; justify-content: center;
    letter-spacing: 0.2px;
  }

  .contact-panel { position: absolute; left: 0; top: 0; }
  .holder-name {
    position: absolute; left: 24px; top: 36px;
    font-size: 30px; font-weight: 700; color: var(--reverse-text);
  }
  .holder-role {
    position: absolute; left: 24px; top: 76px;
    font-size: 24px; color: var(--reverse-text);
  }
  .holder-rule {
    position: absolute; left: 17px; top: 123px; width: 310px; height: 2px;
    background: var(--reverse-text);
  }
  .contact-line {
    position: absolute; left: 24px; display: flex; align-items: center; gap: 12px;
    color: var(--reverse-text); font-size: 20px;
  }
  .contact-line--phone { top: 220px; }
  .contact-line--email { top: 302px; font-size: 17px; }
  .contact-line svg { flex: none; }

  .card--front .brand-mark { left: 530px; top: 98px; width: 166px; height: 166px; }
  .card--front .brand-name { left: 418px; width: 400px; top: 306px; font-size: 31px; }
</style>
</head>
<body>
<main class="canvas">

  <section class="card card--back" aria-label="Card back">
    <span class="brand-mark" aria-hidden="true"></span>
    <div class="brand-name">MARLOW CREST GROUP</div>
    <div class="card-band">glen@marlowcrest-example.com.au</div>
  </section>

  <section class="card card--front" aria-label="Card front">
    <svg class="contact-panel" width="849" height="449" viewBox="0 0 849 449" aria-hidden="true">
      <path d="M0 0 H279 A302 302 0 0 1 279 449 H0 Z" fill="var(--ink)"/>
    </svg>
    <div class="holder-name">Glen Varley</div>
    <div class="holder-role">Managing Director</div>
    <div class="holder-rule"></div>

    <div class="contact-line contact-line--phone">
      <svg width="28" height="30" viewBox="0 0 24 24" aria-hidden="true">
        <path fill="var(--reverse-text)" d="M6.6 2.2l2.6 3.9c.3.5.2 1.1-.2 1.5L7.6 8.9c1 2.8 3.3 5.7 6 7.3l1.4-1.3c.4-.4 1-.4 1.5-.1l3.9 2.6c.5.3.6 1 .3 1.5l-1.3 2c-.5.8-1.5 1.2-2.4.9C10.3 19.7 4.5 13.5 2.9 6.6c-.2-.9.2-1.8 1-2.3l1.9-1.2c.3-.2.6-.1.8.1z"/>
      </svg>
      <span>0437259064</span>
    </div>

    <div class="contact-line contact-line--email">
      <svg width="30" height="30" viewBox="0 0 24 24" aria-hidden="true" fill="none" stroke="var(--reverse-text)" stroke-width="1.6">
        <circle cx="12" cy="12" r="10"/>
        <ellipse cx="12" cy="12" rx="4.5" ry="10"/>
        <path d="M2 12h20M3.5 7h17M3.5 17h17"/>
      </svg>
      <span>glen@marlowcrest-example.com.au</span>
    </div>

    <span class="brand-mark" aria-hidden="true"></span>
    <div class="brand-name">MARLOW CREST GROUP</div>
  </section>

</main>
</body>
</html>
```